Media Browser and player web application

I need to redesign a web application that enables to browse a media server (Tellavo) contents (images, audio, video) and play it in a web player.

Current implementation of the application can be seen at: http://www.tellavohub.example/content/demonstration-tellavo-pro-online-media-browser

This refresh is aiming to:
1) make the application simpler, based on typology (think Windows Metro style, VidSpire, Flickora); a simple fan concept is here: http://dex.lomarquin.example/tellavo/
2) make the application work on desktop as well as touch screen devices (ie no hover functionality, no pagination, large touch controls)
3) fast (remove unnecessary animations)
4) design with the app being responsive in mind

The attached UX designs show the basic flows in the application. Please note that the placement of controls (for example) is not set in stone and I welcome your input on the layout.

Ideally the default theme will be dark. Items' thumbnails will be square place holders, with images fit in them depending on the item icons' aspect ratio.

Also attaching the product's logo (Tellavo) and icon. The web application's name is ClipRover (or Tellavo ClipRover), so it should be included in the design (the UX designs include place holder Tellavo logo in the left top corner).

The main categories for each file type are (you will have to provide an icon for each of these):
- Audio: Albums, Artists, Album artists, Folders, Genres, Composers, Titles, Random music, Random albums, Last listened, Playlists, Online
- Image: Albums, Folders, Year, Month, Playlists, Online
- Video: Titles, Movies, Series, Folders, Last viewed, Last added, Genres, Actors, Directors, Producers, Release years, Playlists, Online
Updates

Target Market(s)

Mostly tech enthusiasts who want to stream their media over the internet to their devices.

Industry/Entity Type

Artists

Requirements
Must have
• Designs for all the provided UX designs
Touch-friendly web application design
High-res (Retina) assets
Light, type based Metro-like design
Nice to have
• Responsive web version
Dark and Light theme switching.
Should not have
• Chrome
Heavy graphics (eg backgrounds) that take time to load

```html
<!DOCTYPE html>
<html lang="en">
<head>
<meta charset="utf-8">
<title>ClipRover – Search</title>
<link rel="stylesheet" href="https://fonts.googleapis.com/css2?family=Lato:wght@300;400;700&display=swap">
<style>
:root{
  --page:#1e1e1e;
  --bar:#121212;
  --tile:#262626;
  --gold:#d9a21f;
  --gold-light:#e8b935;
  --text:#e6e6e6;
  --muted:#9a9a9a;
  --modal:#3f3f3f;
  --field:#000;
  --scrim:rgba(0,0,0,.64);
}
*{box-sizing:border-box;margin:0;padding:0}
html,body{width:1200px;height:724px;overflow:hidden;background:var(--page);font-family:'Lato',sans-serif;color:var(--text)}
.app{position:relative;width:1200px;height:724px}
.topbar{position:absolute;left:0;top:0;width:1200px;height:32px;background:var(--bar)}
.welcome{position:absolute;right:112px;top:10px;font-size:11px;color:var(--gold);display:flex;align-items:center;gap:5px}
.welcome .caret{font-size:9px;margin-left:4px}
.brand{position:absolute;left:95px;top:58px;display:flex;align-items:center;gap:10px}
.brand-mark{width:28px;height:28px;background:var(--gold);border-radius:4px}
.brand-name{font-weight:700;font-size:21px;letter-spacing:1.5px;color:#cfcfcf}
.toolbar{position:absolute;top:41px;left:781px;display:flex;gap:7px}
.tool{width:56px;height:56px;background:var(--gold);display:flex;flex-direction:column;align-items:center;justify-content:space-between;padding:9px 0 4px;font-size:11px;color:#fff}
.tool svg{width:18px;height:18px;fill:#fff}
.crumbs{position:absolute;left:108px;top:120px;font-size:16px;color:var(--muted)}
.crumbs .current{color:var(--gold)}
.grid{position:absolute;left:95px;top:172px;display:grid;grid-template-columns:repeat(6,153px);column-gap:15px;row-gap:15px}
.tile{position:relative;width:153px;height:197px;background:var(--tile)}
.tile .toggle{position:absolute;right:6px;top:6px;width:25px;height:25px;background:var(--gold);color:#fff;font-size:18px;line-height:24px;text-align:center}
.tile .thumb{position:absolute;left:6px;top:37px;width:141px;height:79px}
.tile .play{position:absolute;left:56px;top:18px;width:30px;height:30px;background:rgba(0,0,0,.45)}
.tile .play svg{width:30px;height:30px;fill:var(--gold)}
.tile .info{position:absolute;right:6px;top:122px;width:25px;height:25px;background:#3a3a3a;color:#fff;font-style:italic;font-size:14px;line-height:25px;text-align:center;font-family:Georgia,serif}
.tile .caption{position:absolute;left:6px;top:167px;font-size:11px;line-height:13px;color:#fff}
.tile .caption span{color:var(--gold)}
.poster{position:absolute;left:0;top:0;width:153px;height:153px;background:linear-gradient(160deg,#6d8ea8,#2c4156 55%,#1b2a35)}
.tile.folder{background:var(--gold)}
.tile.folder svg{position:absolute;left:54px;top:58px;width:48px;height:40px}
.tile .label{position:absolute;left:18px;top:170px;font-size:12px}
.t1{background:linear-gradient(135deg,#2f4f73,#8aa7c2)}
.t2{background:linear-gradient(135deg,#c9c4bb,#6b3a33)}
.t3{background:linear-gradient(135deg,#2b3a4d,#b8aa90)}
.t4{background:linear-gradient(135deg,#4e6a7d,#c9c2b5)}
.t5{background:linear-gradient(135deg,#a3292b,#5d6e82)}
.t6{background:linear-gradient(135deg,#2d6da0,#e2c93a)}
.footer{position:absolute;left:0;top:673px;width:1200px;height:51px;background:#181818}
.powered{position:absolute;right:105px;top:18px;font-size:12px;color:var(--muted);display:flex;align-items:center;gap:10px}
.powered i{display:block;width:21px;height:21px;background:#666}
.scrim{position:absolute;inset:0;background:var(--scrim)}
.modal{position:absolute;left:289px;top:253px;width:623px;height:245px;background:var(--modal)}
.modal h2{position:absolute;left:32px;top:30px;font-weight:300;font-size:20px;color:#e8e8e8}
.search{position:absolute;left:33px;top:94px;display:flex}
.search .field{width:451px;height:40px;background:var(--field);color:#d8d8d8;font-size:20px;font-weight:300;padding-left:15px;line-height:40px}
.search .go{width:93px;height:40px;background:linear-gradient(90deg,var(--gold),var(--gold-light));display:flex;align-items:center;justify-content:center}
.search .go svg{width:22px;height:22px}
</style>
</head>
<body>
<div class="app">
  <header class="topbar"><div class="welcome">● Welcome Username <span class="caret">▼</span></div></header>
  <div class="brand"><span class="brand-mark"></span><span class="brand-name">CLIPROVER</span></div>
  <nav class="toolbar">
    <div class="tool"><svg viewBox="0 0 18 18"><rect x="1" y="2" width="16" height="3"/><rect x="1" y="7.5" width="16" height="3"/><rect x="1" y="13" width="16" height="3"/></svg>List View</div>
    <div class="tool"><svg viewBox="0 0 18 18"><rect x="1" y="2" width="3" height="3"/><rect x="6" y="2" width="11" height="3"/><rect x="1" y="7.5" width="3" height="3"/><rect x="6" y="7.5" width="11" height="3"/><rect x="1" y="13" width="3" height="3"/><rect x="6" y="13" width="11" height="3"/></svg>Queue</div>
    <div class="tool"><svg viewBox="0 0 18 18"><rect x="7" y="1" width="4" height="16"/><rect x="1" y="7" width="16" height="4"/></svg>Enqueue</div>
    <div class="tool"><svg viewBox="0 0 18 18"><path d="M4 2l12 7-12 7z"/></svg>Play All</div>
    <div class="tool"><svg viewBox="0 0 18 18"><circle cx="7" cy="7" r="5" fill="none" stroke="#fff" stroke-width="2.5"/><path d="M10.5 10.5l6 6" stroke="#fff" stroke-width="3"/></svg>Search</div>
  </nav>
  <div class="crumbs">Home &gt; Video &gt; <span class="current">Folders</span></div>

  <main class="grid">
    <div class="tile"><div class="poster" role="img" aria-label="Game cover artwork"></div><div class="label">The Best from Skyreach</div></div>
    <div class="tile folder"><svg viewBox="0 0 48 40" fill="none" stroke="#fff" stroke-width="2.5"><rect x="3" y="14" width="42" height="24"/><path d="M3 14l40-10 2 7"/></svg></div>
    <div class="tile"><div class="toggle">−</div><div class="thumb t1" role="img" aria-label="Video scene still"><div class="play"><svg viewBox="0 0 30 30"><path d="M11 9l10 6-10 6z"/></svg></div></div><div class="info">i</div><div class="caption">Very Long Scene N..., <span>2013<br>4:35:27</span></div></div>
    <div class="tile"><div class="toggle">+</div><div class="thumb t2" role="img" aria-label="Video scene still"><div class="play"><svg viewBox="0 0 30 30"><path d="M11 9l10 6-10 6z"/></svg></div></div><div class="info">i</div><div class="caption">Very Long Scene N..., <span>2013<br>4:35:27</span></div></div>
    <div class="tile"><div class="toggle">−</div><div class="thumb t3" role="img" aria-label="Video scene still"><div class="play"><svg viewBox="0 0 30 30"><path d="M11 9l10 6-10 6z"/></svg></div></div><div class="info">i</div><div class="caption">Very Long Scene N..., <span>2013<br>4:35:27</span></div></div>
    <div class="tile"><div class="toggle">+</div><div class="thumb t4" role="img" aria-label="Video scene still"><div class="play"><svg viewBox="0 0 30 30"><path d="M11 9l10 6-10 6z"/></svg></div></div><div class="info">i</div><div class="caption">Very Long Scene N..., <span>2013<br>4:35:27</span></div></div>
    <div class="tile"><div class="toggle">+</div><div class="thumb t5" role="img" aria-label="Video scene still"><div class="play"><svg viewBox="0 0 30 30"><path d="M11 9l10 6-10 6z"/></svg></div></div><div class="info">i</div><div class="caption">Very Long Scene N..., <span>2013<br>4:35:27</span></div></div>
    <div class="tile"><div class="toggle">+</div><div class="thumb t1" role="img" aria-label="Video scene still"><div class="play"><svg viewBox="0 0 30 30"><path d="M11 9l10 6-10 6z"/></svg></div></div><div class="info">i</div><div class="caption">Very Long Scene N..., <span>2013<br>4:35:27</span></div></div>
    <div class="tile"><div class="toggle">+</div><div class="thumb t3" role="img" aria-label="Video scene still"><div class="play"><svg viewBox="0 0 30 30"><path d="M11 9l10 6-10 6z"/></svg></div></div><div class="info">i</div><div class="caption">Very Long Scene N..., <span>2013<br>4:35:27</span></div></div>
    <div class="tile"><div class="toggle">+</div><div class="thumb t4" role="img" aria-label="Video scene still"><div class="play"><svg viewBox="0 0 30 30"><path d="M11 9l10 6-10 6z"/></svg></div></div><div class="info">i</div><div class="caption">Very Long Scene N..., <span>2013<br>4:35:27</span></div></div>
    <div class="tile"><div class="toggle">+</div><div class="thumb t2" role="img" aria-label="Video scene still"><div class="play"><svg viewBox="0 0 30 30"><path d="M11 9l10 6-10 6z"/></svg></div></div><div class="info">i</div><div class="caption">Very Long Scene N..., <span>2013<br>4:35:27</span></div></div>
    <div class="tile"><div class="toggle">+</div><div class="thumb t6" role="img" aria-label="Video scene still"><div class="play"><svg viewBox="0 0 30 30"><path d="M11 9l10 6-10 6z"/></svg></div></div><div class="info">i</div><div class="caption">Very Long Scene N..., <span>2013<br>4:35:27</span></div></div>
  </main>

  <footer class="footer"><div class="powered">Powered by <i></i></div></footer>

  <div class="scrim"></div>
  <section class="modal" aria-label="Search for videos">
    <h2>Search for videos</h2>
    <div class="search">
      <div class="field">Video Name</div>
      <div class="go"><svg viewBox="0 0 22 22"><circle cx="9" cy="9" r="6" fill="none" stroke="#fff" stroke-width="3"/><path d="M13.5 13.5l6 6" stroke="#fff" stroke-width="3.5" stroke-linecap="round"/></svg></div>
    </div>
  </section>
</div>
</body>
</html>
```